Harbourline Plumbing business card full re design & logo design

Harbourline Plumbing is a Sydney based mechanical plumbing contractor company.
We would like a full redesign with new logo etc which we can take to a future website, uniforms, vehicle sign writing etc.
Blue is my preferred choice of colour but i would be open to see a couple of alternatives thrown in the mix to see how they compare. I am open to see on white cards, black cards etc. Open to many new ideas.
Please see attached original business cards which have been used for the last 5 years.

Target Market(s)

Mechanical services industry.

Industry/Entity Type

Plumbing

Contact Information for Business Card

Colin Ferraday
Director

Mob: 0427 560 918
Email: colin@harbourlineplumbing.net.au
PO BOX 716
Wendale NSW 2158
Lic: 583926d

Logo Text

Harbourline Plumbing

Font styles to use
Sans Serif

Colors
0655a3
3276b5
0792cd
33a6d7
85cae6
000000
333333
474747

Requirements
Must have
• Things that make it very professional and very well presented.
Nice to have
• Same description or very similar to attached uploaded file
Should not have
• Anything that makes it look unprofessional or cartoony.

```html
<!DOCTYPE html>
<html lang="en">
<head>
<meta charset="utf-8">
<title>Harbourline Plumbing – Business Card</title>
<link rel="stylesheet" href="https://fonts.googleapis.com/css2?family=Ubuntu:wght@400;500;700&display=swap">
<style>
  :root {
    --blue-deep: #0655a3;
    --blue-mid: #3276b5;
    --blue-bright: #0792cd;
    --blue-light: #33a6d7;
    --blue-pale: #85cae6;
    --black: #000000;
    --grey-dark: #333333;
    --grey: #474747;
    --white: #ffffff;
    --paper: #f4f5f6;
    --stage: #e6e8eb;
  }
  * { box-sizing: border-box; margin: 0; padding: 0; }
  html, body { width: 1200px; height: 780px; overflow: hidden; }
  body {
    background: var(--stage);
    font-family: "Ubuntu", sans-serif;
    display: flex;
    align-items: center;
    justify-content: center;
    gap: 48px;
  }
  .card {
    position: relative;
    width: 540px;
    height: 328px;
    background: linear-gradient(180deg, var(--white), var(--paper));
    box-shadow: 0 6px 18px rgba(0,0,0,0.18);
    overflow: hidden;
  }
  .card__white { position: absolute; left: 0; right: 0; top: 0; height: 158px; display: flex; align-items: center; }
  .card__band {
    position: absolute; left: 0; right: 0; top: 158px; height: 120px;
    background: linear-gradient(90deg, var(--blue-deep), var(--blue-bright));
    color: var(--white);
  }
  .card__strip {
    position: absolute; left: 0; right: 0; top: 284px; height: 34px;
    background: var(--black); color: var(--white);
    display: flex; align-items: center; justify-content: center;
    font-size: 15px; font-weight: 500; letter-spacing: 1px;
  }
  .card__edge { position: absolute; left: 0; right: 0; top: 278px; height: 6px; background: var(--white); }
  .card__foot { position: absolute; left: 0; right: 0; top: 318px; height: 10px; background: var(--blue-mid); }

  .brand { display: flex; align-items: center; gap: 14px; }
  .brand__dot { width: 34px; height: 34px; border-radius: 50%; background: var(--blue-bright); }
  .brand__name { font-size: 30px; font-weight: 700; color: var(--blue-deep); letter-spacing: 1px; text-transform: uppercase; }

  .card--front .card__white { padding-left: 70px; }
  .contact { display: flex; align-items: center; height: 100%; padding: 0 30px; }
  .person { text-align: right; width: 190px; padding-right: 20px; border-right: 1.5px solid rgba(255,255,255,0.75); }
  .person__name { font-size: 22px; font-weight: 500; }
  .person__role, .person__lic { font-size: 14px; margin-top: 3px; }
  .details { list-style: none; padding-left: 20px; font-size: 13px; }
  .details li { display: flex; align-items: center; gap: 8px; margin: 5px 0; }
  .details svg { width: 16px; height: 16px; flex: none; }

  .card--back .card__white { justify-content: center; }
  .services { padding: 12px 34px; }
  .services__title { font-size: 16px; font-weight: 500; letter-spacing: 1.5px; text-transform: uppercase; }
  .services__lead { font-size: 17px; font-weight: 700; margin: 8px 0 6px; }
  .services__cols { display: flex; gap: 34px; }
  .services__list { list-style: none; font-size: 13.5px; padding-right: 24px; }
  .services__list + .services__list { border-left: 1.5px solid rgba(255,255,255,0.75); padding-left: 24px; }
  .services__list li { display: flex; align-items: center; gap: 8px; margin: 3px 0; }
  .services__list li::before { content: ""; width: 7px; height: 7px; border-radius: 50%; background: var(--white); }
</style>
</head>
<body>

<section class="card card--front" aria-label="Business card front">
  <div class="card__white">
    <div class="brand">
      <span class="brand__dot"></span>
      <span class="brand__name">Harbourline Plumbing</span>
    </div>
  </div>
  <div class="card__band">
    <div class="contact">
      <div class="person">
        <p class="person__name">Colin Ferraday</p>
        <p class="person__role">Director</p>
        <p class="person__lic">Lic: 583926d</p>
      </div>
      <ul class="details">
        <li>
          <svg viewBox="0 0 16 16"><rect x="0.5" y="0.5" width="15" height="15" rx="2" fill="none" stroke="#fff"/><rect x="5" y="3" width="6" height="10" rx="1" fill="#fff"/></svg>
          0427 560 918
        </li>
        <li>
          <svg viewBox="0 0 16 16"><rect x="0.5" y="0.5" width="15" height="15" rx="2" fill="none" stroke="#fff"/><rect x="3" y="4.5" width="10" height="7" fill="none" stroke="#fff"/><path d="M3 4.5 L8 8.5 L13 4.5" fill="none" stroke="#fff"/></svg>
          colin@harbourlineplumbing.net.au
        </li>
        <li>
          <svg viewBox="0 0 16 16"><rect x="0.5" y="0.5" width="15" height="15" rx="2" fill="none" stroke="#fff"/><path d="M8 13 C5 9.5 4.5 8 4.5 6.5 A3.5 3.5 0 0 1 11.5 6.5 C11.5 8 11 9.5 8 13 Z" fill="#fff"/><circle cx="8" cy="6.5" r="1.3" fill="#0792cd"/></svg>
          PO BOX 716, Wendale NSW 2158
        </li>
      </ul>
    </div>
  </div>
  <div class="card__edge"></div>
  <div class="card__strip">MECHANICAL PIPING | CHW | HW | CW | REFRIG</div>
  <div class="card__foot"></div>
</section>

<section class="card card--back" aria-label="Business card back">
  <div class="card__white">
    <div class="brand">
      <span class="brand__dot"></span>
      <span class="brand__name">Harbourline Plumbing</span>
    </div>
  </div>
  <div class="card__band">
    <div class="services">
      <p class="services__title">Mechanical Plumbing Services</p>
      <p class="services__lead">Specialising in:</p>
      <div class="services__cols">
        <ul class="services__list">
          <li>Make Good</li>
          <li>Refurbishment</li>
          <li>Tenancy Fit Out</li>
        </ul>
        <ul class="services__list">
          <li>Plant Room Works</li>
          <li>Shut Downs</li>
          <li>Change Overs</li>
        </ul>
      </div>
    </div>
  </div>
  <div class="card__edge"></div>
  <div class="card__strip">HARBOURLINE have the SOLUTION</div>
  <div class="card__foot"></div>
</section>

</body>
</html>
```